Infectious Diseases Research Laboratory Needs Business Card

We need a business card for an academic research laboratory based in Kansas City called MORVEK. The full lab name is Microbial Dose-Response/Exposure Bridging Studies Laboratory, but this does not need to be incorporated. We study novel ways to optimize the treatment of multidrug-resistant bacterial infections ("superbugs") throughout the entire biomedical research spectrum (from benchtop to bedside). The name MORVEK is not only an acronym for our lab name, but also represents our desire to make discoveries and explore the unknown (the stars, if you well). It also serves as an ode to the state of Kansas motto where we are based, ad astra per aspera ("to the stars, through difficulty").

Target Market(s)

Pharmaceutical companies, researchers

Industry/Entity Type

Pharmaceutical

Contact Information for Business Card

The business card should incorporate and complement our new logo (see uploaded files). Double-sided designs are preferred. Looking for something modern, but professional.

Font styles to use
Sans Serif

Requirements
Must have
• Double-sided. One side would ideally be a solid color incorporating logo and the other should also have the logo (smaller), but incorporate staff information.
• Color codes:
• Red: #F04C51
• Blue: #3477B5
• Gray: #808285

```html
<!DOCTYPE html>
<html lang="en">
<head>
<meta charset="utf-8">
<title>MORVEK Business Card</title>
<link href="https://fonts.googleapis.com/css2?family=Montserrat:wght@300;400;500&display=swap" rel="stylesheet">
<style>
  :root {
    --backdrop: #ecebe8;
    --navy: #34507f;
    --red: #d63a42;
    --red-light: #e2474e;
    --paper: #f4f4f5;
    --gray: #d9dadc;
    --ink: #22304d;
    --white: #ffffff;
  }
  html, body {
    margin: 0;
    padding: 0;
    overflow: hidden;
  }
  body {
    width: 1200px;
    height: 800px;
    background: var(--backdrop);
    font-family: "Montserrat", sans-serif;
  }
  .card-set {
    position: relative;
    width: 1200px;
    height: 800px;
  }
  .card {
    position: absolute;
    top: 120px;
    width: 330px;
    height: 560px;
    box-shadow: 0 10px 30px rgba(0,0,0,0.18);
  }
  .card--front { left: 215px; }
  .card--back { left: 655px; }
  .card svg { display: block; }
  .wordmark {
    font-family: "Montserrat", sans-serif;
    font-weight: 300;
    letter-spacing: 6px;
  }
  .staff-name {
    font-family: "Montserrat", sans-serif;
    font-weight: 500;
    letter-spacing: 1px;
  }
  .staff-role, .contact-line {
    font-family: "Montserrat", sans-serif;
    font-weight: 400;
  }
</style>
</head>
<body>
<main class="card-set">

  <!-- Front side -->
  <section class="card card--front" aria-label="Card front">
    <svg width="330" height="560" viewBox="0 0 330 560" xmlns="http://www.w3.org/2000/svg">
      <rect class="front-base" width="330" height="560" fill="var(--navy)"/>
      <path class="front-top-band" d="M90 0 L132 72 Q142 88 162 88 L330 88 L330 0 Z" fill="var(--gray)"/>
      <path class="front-top-block" d="M112 0 L142 50 Q150 64 168 64 L330 64 L330 0 Z" fill="var(--red)"/>
      <path class="front-bottom-block" d="M0 392 Q0 362 28 362 L222 362 Q242 362 254 378 L330 470 L330 560 L0 560 Z" fill="var(--red)"/>
      <g class="front-logo">
        <circle cx="86" cy="238" r="14" fill="var(--gray)"/>
        <text class="wordmark" x="110" y="248" font-size="30" fill="var(--gray)">MORVEK</text>
      </g>
    </svg>
  </section>

  <!-- Back side -->
  <section class="card card--back" aria-label="Card back">
    <svg width="330" height="560" viewBox="0 0 330 560" xmlns="http://www.w3.org/2000/svg">
      <rect class="back-base" width="330" height="560" fill="var(--paper)"/>

      <path class="back-top-frame" d="M70 0 L330 0 L330 320 L205 320 Q186 320 176 306 L80 190 Q70 178 70 160 Z" fill="var(--navy)"/>
      <path class="back-top-block" d="M84 0 L330 0 L330 228 L168 228 L96 150 Q84 137 84 120 Z" fill="var(--red-light)"/>

      <path class="back-bottom-block" d="M0 300 L128 300 Q148 300 160 316 L256 440 Q264 452 264 468 L264 560 L0 560 Z" fill="var(--red)"/>
      <path class="back-name-band" d="M0 336 L156 336 L185 374 L0 374 Z" fill="var(--navy)"/>

      <g class="back-logo">
        <circle cx="124" cy="92" r="11" fill="var(--white)"/>
        <text class="wordmark" x="143" y="101" font-size="24" fill="var(--white)">MORVEK</text>
      </g>

      <text class="staff-name" x="18" y="354" font-size="15" fill="var(--ink)">ELENA MARSH</text>
      <text class="staff-role" x="18" y="368" font-size="10" fill="var(--ink)">Creative Designer</text>

      <g class="contact-details" fill="var(--white)" font-size="10.5">
        <text class="contact-line" x="18" y="404">phone : 816 . 5550 . 1427</text>
        <text class="contact-line" x="18" y="422">email  : hello@morveklab.com</text>
        <text class="contact-line" x="18" y="440">web    : www.morveklabresearch.org</text>
        <text class="contact-line" x="18" y="466">home  : 41 Orchard Lane, West Hill</text>
        <text class="contact-line" x="18" y="482">KC 64108 USA</text>
      </g>
    </svg>
  </section>

</main>
</body>
</html>
```